PWF - world groomers association website

Pacific Whisker Federation (PWF) is a new association located in USA, start the first project in South Korea. As now we do the following business:
1. We supply dog grooming education
2. We certify dog groomers
3. We host dog grooming education events
4. We organize grooming trade show

The design:
Because this organization is related to dog grooming, so beautiful groomed dog images are important. I will upload some well groomed dog images. I want you are able to put all these images or some of the images together either nice color or just layout of the images. I want the first page impressive. This business is related to grooming education, so I want our customers get impressed by visiting our website and decide to contact us for their continuing education. Also since this is an association, I want the website to be some level of institutional. Background layout and images catch eyes, but the content area simple and clear.

I want to be able to edit my site by adding images and edit the contents by myself in a easy way.

I need 5 pages now, but I may need to add more pages, but not more than 8 pages.

www.tollmarden.com is the site I really like.

Thanks.

• consistent tune on every page
• several well-groomed dogs, I can provide images

```html
<!DOCTYPE html>
<html lang="en">
<head>
<meta charset="utf-8">
<title>Become Member – Pacific Whisker Federation</title>
<link href="https://fonts.googleapis.com/css2?family=Oswald:wght@400;500;600&family=Open+Sans:wght@400;600;700&display=swap" rel="stylesheet">
<style>
:root{
  --ink:#222;
  --text:#444;
  --muted:#777;
  --line:#c9c9c9;
  --green:#a7c64b;
  --green-soft:#c5d97c;
  --teal:#80c9c0;
  --blue:#3a78c2;
  --band:#86aad2;
  --red:#e0312f;
  --footer:#353535;
  --white:#fff;
}
*{box-sizing:border-box;margin:0;padding:0}
html,body{width:1200px;height:3390px;overflow:hidden;background:var(--white)}
body{font-family:"Open Sans",Arial,sans-serif;color:var(--text);font-size:13px}
.page{position:relative;width:1200px;height:3390px;overflow:hidden}
.abs{position:absolute}

.topbar{left:0;top:0;width:1200px;height:80px;background:var(--white);border-top:4px solid #8fb3d6}
.nav{left:271px;top:28px;display:flex;gap:19px;font-family:"Oswald",sans-serif;font-size:14px;font-weight:500;color:var(--ink);align-items:center}
.nav .active{color:var(--green)}
.brand{left:88px;top:18px;width:150px;height:150px;border-radius:50%;background:var(--white);box-shadow:0 0 0 4px #e8eef4;display:flex;align-items:center;justify-content:center;font-family:"Oswald",sans-serif;font-weight:600;font-size:40px;color:#1f3f66;z-index:3}
.hero{left:0;top:80px;width:1200px;height:293px;background:linear-gradient(90deg,#8c8a86 0%,#b9b2a8 25%,#e9e6e1 50%,#d9d5cf 65%,#5d5a57 85%,#3e3c3a 100%)}
.hero-title{left:0;top:176px;width:1200px;text-align:center;font-family:"Oswald",sans-serif;font-weight:600;font-size:62px;color:var(--white);letter-spacing:1px;text-shadow:0 2px 6px rgba(0,0,0,.35)}
.dots{left:540px;top:336px;display:flex;gap:8px}
.dots span{width:22px;height:4px;background:var(--white)}
.dots span.on{background:var(--green)}

.crumb{left:99px;top:401px;font-family:"Oswald",sans-serif;font-size:14px;color:var(--ink)}
.crumb b{color:var(--blue);font-weight:400}
.crumb-rule{left:99px;top:430px;width:1002px;height:1px;background:#ddd}
.page-title{left:99px;top:470px;font-family:"Oswald",sans-serif;font-weight:500;font-size:23px;color:var(--ink)}
.intro{left:99px;top:518px;width:1002px;font-size:11.5px;line-height:22px;color:var(--muted)}
.intro a{color:var(--blue);font-weight:600;text-decoration:none}
.form-lead{left:99px;top:648px;font-weight:700;font-size:15px;color:var(--ink)}
.section-head{font-weight:700;font-size:15px;color:var(--ink);letter-spacing:.3px}
.required{left:470px;top:688px;color:var(--red);font-size:12px;font-weight:600}

.form{left:0;width:1200px}
.row{display:flex;align-items:center;height:46.6px}
.row label.k{width:418px;text-align:right;font-size:12.5px;color:var(--text);line-height:17px}
.field{margin-left:52px;height:34px;border:1px solid var(--line);background:var(--white)}
.w-l{width:463px}.w-m{width:389px}.w-s{width:244px}
.choices{margin-left:52px;display:flex;align-items:center;font-size:12.5px;color:var(--text)}
.box{display:inline-block;width:22px;height:22px;border:1px solid var(--line);background:var(--white);vertical-align:middle;margin-right:18px}
.choice{display:flex;align-items:center;width:230px}

.secure{font-weight:700;font-size:30px;color:#4a4a4a;display:flex;align-items:center;gap:10px}
.secure i{display:block;width:44px;height:44px;background:#1d4d8c}

.set{position:absolute;left:470px;width:463px;border:1px solid var(--line);padding:10px 18px}
.set legend{font-size:12.5px;color:var(--text);padding:0 6px}
.set .opt{display:flex;align-items:center;font-size:12.5px;height:28px}
.set .opt .box{margin-right:14px;width:20px;height:20px}

.band{left:99px;width:1002px;height:41px;background:var(--band);color:var(--white);font-weight:700;font-size:12.5px;padding:12px 22px;letter-spacing:.2px}
.agree{left:99px;top:2594px;width:1002px;font-size:11.5px;color:var(--text);line-height:26px}
.agree .amount{display:inline-block;width:78px;height:22px;border:1px solid #f2a3a3;vertical-align:middle;margin:0 10px}
.agree .name-in{display:inline-block;width:224px;height:20px;border:1px solid #f2a3a3;vertical-align:middle;margin:0 12px 0 6px}
.bio{left:97px;top:2762px;width:687px;height:153px;border:1px solid var(--line)}
.btn{top:2940px;height:32px;color:var(--white);font-family:"Oswald",sans-serif;font-size:12px;letter-spacing:.5px;display:flex;align-items:center;justify-content:center;border-radius:3px}
.btn-submit{left:633px;width:72px;background:var(--green-soft)}
.btn-reset{left:714px;width:68px;background:var(--teal)}

.footer{left:0;top:3080px;width:1200px;height:310px;background:var(--footer);color:#d8d8d8}
.foot-col{position:absolute;top:44px}
.foot-col h4{font-family:"Oswald",sans-serif;font-weight:500;font-size:15px;color:var(--white);margin-bottom:14px;letter-spacing:.3px}
.foot-col ul{list-style:none;font-size:12px;line-height:20.5px}
.foot-col p{font-size:12px;line-height:20px;width:260px}
.news-in{margin-top:16px;width:269px;height:34px;background:var(--white);color:#888;font-size:11px;padding:9px 10px}
.news-btn{margin-top:15px;width:93px;height:30px;background:var(--green);color:var(--white);font-family:"Oswald",sans-serif;font-size:12px;display:flex;align-items:center;justify-content:center}
.contact li{display:flex;align-items:flex-start;gap:20px;margin-bottom:12px}
.contact svg{flex:none;margin-top:3px}
.foot-rule{position:absolute;left:97px;top:238px;width:1006px;height:1px;background:#4a4a4a}
.copy{position:absolute;left:97px;top:264px;font-size:11.5px;color:#cfcfcf}
.social{position:absolute;left:958px;top:252px;display:flex;gap:9px}
.social span{width:32px;height:32px;border:2px solid #d0d0d0;border-radius:50%}
</style>
</head>
<body>
<div class="page">

  <header>
    <div class="abs topbar"></div>
    <div class="abs brand">PWF</div>
    <nav class="abs nav">
      <span>Home</span><span>Event</span><span>Our Partners</span><span>Our Certifiers</span>
      <span>Grooming Education</span><span>Grooming Product</span><span>Contact Us</span>
      <span class="active">Become Member</span><span>Certifications</span>
      <svg width="14" height="14" viewBox="0 0 14 14"><circle cx="6" cy="6" r="4.5" fill="none" stroke="#222" stroke-width="2"/><line x1="9.3" y1="9.3" x2="13" y2="13" stroke="#222" stroke-width="2"/></svg>
    </nav>
    <div class="abs hero" role="img" aria-label="Photo of a groomer trimming a white poodle on a grooming table"></div>
    <h1 class="abs hero-title">BECOME MEMBER</h1>
    <div class="abs dots"><span class="on"></span><span></span><span></span><span></span></div>
  </header>

  <main>
    <div class="abs crumb">HOME &nbsp;&gt;&gt;&nbsp; <b>BECOME MEMBER</b></div>
    <div class="abs crumb-rule"></div>
    <h2 class="abs page-title">PACIFIC WHISKER FEDERATION MEMBERSHIP APPLICATION FORM</h2>
    <p class="abs intro">Nemo enim ipsam voluptatem quia voluptas sit aspernatur aut odit aut fugit, sed quia consequuntur magni dolores eos qui ratione voluptatem sequi nesciunt. Neque porro quisquam est, qui dolorem ipsum quia dolor sit amet, consectetur, adipisci velit, sed quia non numquam eius modi tempora incidunt ut labore et dolore magnam aliquam quaerat voluptatem. Ut enim ad minima veniam, quis nostrum exercitationem ullam corporis suscipit laboriosam, nisi ut aliquid ex ea commodi consequatur. Quis autem vel eum iure reprehenderit qui in ea voluptate velit esse quam nihil <a>Download Membership Application</a></p>
    <h3 class="abs form-lead">Pacific Whisker Federation Membership Application with payment by credit card :</h3>

    <h3 class="abs section-head" style="left:99px;top:685px">APPLICANT PERSONAL INFORMATION</h3>
    <div class="abs required">* Required Information</div>

    <div class="abs form" style="top:725px">
      <div class="row"><label class="k">*Applicant's Name:</label><span class="field w-l"></span></div>
      <div class="row"><label class="k">*Address:</label><span class="field w-l"></span></div>
      <div class="row"><label class="k">*City, State-Prov:</label><span class="field w-l"></span></div>
      <div class="row"><label class="k">*Zip-Postal Code:</label><span class="field w-s"></span></div>
      <div class="row"><label class="k">*Country:</label><span class="field w-s"></span></div>
      <div class="row"><label class="k">*Date of Birth:</label><span class="field w-s"></span></div>
      <div class="row"><label class="k">*Home Phone:</label><span class="field w-l"></span></div>
      <div class="row"><label class="k">*Email Address:</label><span class="field w-m"></span></div>
      <div class="row"><label class="k">Mail PWF Membership Materials to:</label>
        <div class="choices"><span class="choice"><span class="box"></span>My Home Address</span><span class="choice"><span class="box"></span>My Salon Address</span></div></div>
      <div class="row"><label class="k">*Salon Name:</label><span class="field w-m"></span></div>
      <div class="row"><label class="k">*Salon Address:</label><span class="field w-m"></span></div>
      <div class="row"><label class="k">*Salon City, State, &amp; Zip:</label><span class="field w-l"></span></div>
      <div class="row"><label class="k">*Salon Phone:</label><span class="field w-m"></span></div>
      <div class="row"><label class="k">*Salon Website:</label><span class="field w-m"></span></div>
      <div class="row"><label class="k">*Your Position:</label><span class="field w-l"></span></div>
      <div class="row"><label class="k">*How Long in Business?</label><span class="field w-l"></span></div>
      <div class="row"><label class="k">*Type of Facility - Land Base or Mobile?</label><span class="field w-l"></span></div>
    </div>

    <h3 class="abs section-head" style="left:99px;top:1551px">YOUR BACKGROUND INFORMATION</h3>
    <div class="abs form" style="top:1591px">
      <div class="row"><label class="k">Number of Years Grooming?</label><span class="field w-l"></span></div>
      <div class="row"><label class="k">Grooming School Graduate?<br>(if yes, Grooming School Name)</label><span class="field w-l"></span></div>
      <div class="row"><label class="k">Apprenticed Under?</label><span class="field w-l"></span></div>
      <div class="row"><label class="k">Accomplishments?</label><span class="field w-l"></span></div>
    </div>

    <div class="abs secure" style="left:97px;top:1820px">SafeLedger<i></i></div>

    <h3 class="abs section-head" style="left:99px;top:1893px">APPLICATION PAYMENT</h3>
    <div class="abs" style="left:0;top:1945px;width:418px;text-align:right;font-size:12.5px">How Do You Propose to Pay?</div>
    <fieldset class="set" style="top:1925px;height:93px">
      <legend>Proposed Payment Method</legend>
      <div class="opt" style="width:190px;float:left"><span class="box"></span>Credit Card Online</div>
      <div class="opt" style="float:left"><span class="box"></span>Credit Card By Fax</div>
      <div class="opt" style="clear:both"><span class="box"></span>Mailing Check/Money Order</div>
    </fieldset>
    <div class="abs" style="left:0;top:2053px;width:418px;text-align:right;font-size:12.5px">Type of Credit Card to process?</div>
    <fieldset class="set" style="top:2034px;height:147px">
      <legend>Credit Card</legend>
      <div class="opt"><span class="box"></span>Northline</div>
      <div class="opt"><span class="box"></span>MeridianPay</div>
      <div class="opt"><span class="box"></span>Crestway Express</div>
      <div class="opt"><span class="box"></span>Horizon Card</div>
    </fieldset>

    <div class="abs form" style="top:2187px">
      <div class="row"><label class="k">Credit Card Number:</label><span class="field w-l"></span></div>
      <div class="row"><label class="k">Name on Credit Card:</label><span class="field w-l"></span></div>
      <div class="row"><label class="k">Billing Address for Card:</label><span class="field w-l"></span></div>
      <div class="row"><label class="k">City, State-Prov, Zip-Postal:</label><span class="field w-l"></span></div>
      <div class="row"><label class="k">Expiration Date - (Example 05/12)</label><span class="field" style="width:133px"></span>
        <span style="margin-left:50px;font-size:12.5px">Security Code (CVS)</span><span class="field" style="margin-left:30px;width:93px"></span></div>
      <div class="row"><label class="k" style="color:var(--red)">Select Fee Based on Residence</label>
        <div class="choices" style="color:var(--red)"><span class="choice" style="width:192px"><span class="box"></span>$90/USA Resident</span><span class="choice"><span class="box"></span>$96/Canadian Resident</span></div></div>
    </div>

    <div class="abs band" style="top:2490px">CHARGE AUTHORIZATION, YOUR CONSENT AND ELECTRONIC SIGNATURE:</div>
    <h3 class="abs section-head" style="left:99px;top:2554px">PAYMENT &amp; LIABILITY AGREEMENT:</h3>
    <div class="abs agree">
      <svg width="12" height="12" viewBox="0 0 12 12" style="vertical-align:middle;margin-right:6px"><rect x=".5" y=".5" width="11" height="11" fill="#fff" stroke="#999"/><path d="M2.5 6l2.5 2.5 4.5-5" fill="none" stroke="#333" stroke-width="1.6"/></svg>I am in agreement and hereby authorize <b>PWF</b> to charge my credit card in the amount of $<span class="amount"></span>in payment for my new membership application fees.<br>
      <b style="color:var(--ink)">Your Name :</b><span class="name-in"></span>By typing my name and entering the total fees to be charged to my credit card, I agree this will serve as my<br>Electronic Signature.
    </div>

    <div class="abs band" style="top:2705px">SHORT BIO ABOUT YOURSELF (OR SEND US AN EMAIL WITH YOUR BIO INFORMATION):</div>
    <div class="abs bio"></div>
    <div class="abs btn btn-submit">SUBMIT</div>
    <div class="abs btn btn-reset">RESET</div>

    <div class="abs secure" style="left:97px;top:2988px">SafeLedger<i></i></div>
  </main>

  <footer class="abs footer">
    <div class="foot-col" style="left:97px">
      <h4>INFORMATION</h4>
      <ul><li>Home</li><li>About</li><li>Education</li><li>Trade Shows</li><li>Certification</li><li>Events</li><li>Contact</li></ul>
    </div>
    <div class="foot-col" style="left:278px">
      <h4>QUICK LINKS</h4>
      <ul><li>Membership Information</li><li>Membership Application</li><li>Find a Groomer</li><li>Member Directory</li><li>Groomer Training</li><li>Articles</li><li>Fundraising</li></ul>
    </div>
    <div class="foot-col" style="left:504px">
      <h4>NEWSLETTER SUBSCRIPTION</h4>
      <p>Register your email Address to get information about us</p>
      <div class="news-in">Email Address</div>
      <div class="news-btn">SUBSCRIBE</div>
    </div>
    <div class="foot-col" style="left:852px">
      <h4>CONTACT US</h4>
      <ul class="contact">
        <li><svg width="14" height="16" viewBox="0 0 14 16"><path d="M7 1a5 5 0 0 0-5 5c0 4 5 9 5 9s5-5 5-9a5 5 0 0 0-5-5z" fill="#ddd"/><circle cx="7" cy="6" r="2" fill="#353535"/></svg><span>48 Harbor Lane, Suite 7<br>90417, Port Hallow</span></li>
        <li><svg width="14" height="14" viewBox="0 0 14 14"><path d="M3 1l2.5 3-1.5 1.5a8 8 0 0 0 4.5 4.5L10 8.5l3 2.5-1.5 2A11 11 0 0 1 1 2.5z" fill="#ddd"/></svg><span>1 555 014 2290</span></li>
        <li><svg width="14" height="14" viewBox="0 0 14 14"><rect x="1" y="4" width="12" height="9" fill="#ddd"/><rect x="3" y="1" width="8" height="4" fill="none" stroke="#ddd" stroke-width="1.5"/><rect x="4" y="8" width="6" height="3" fill="#353535"/></svg><span>1 555 014 3381</span></li>
        <li><svg width="14" height="12" viewBox="0 0 14 12"><rect x="0" y="1" width="14" height="10" fill="#ddd"/><path d="M0 1l7 5 7-5" fill="none" stroke="#353535" stroke-width="1.3"/></svg><span>info@pacificwhiskerfed.com</span></li>
      </ul>
    </div>
    <div class="foot-rule"></div>
    <div class="copy">Copyrights © 2016, Pacific Whisker Federation. All Rights Reserved.</div>
    <div class="social"><span></span><span></span><span></span><span></span></div>
  </footer>

</div>
</body>
</html>
```